Business Card Design

Consultation for design, construction athletic facilities specializing in synthetic turf systems and all weather running track systems.
Motto "True Owner Representation"
New Company that we'd like to highlight the LOGO first and foremost with the colors of the background and font as primary colors of the card too if possible. I've also attached a typical larger project design layout that could be used in the background to highlight our design and construction specialty.
Website is something we want very noticeable for driving traffic.
Target Market(s)
Athletic Directors, Designers, Government and Military, Contractors
Industry/Entity Type
Construction
Contact Information for Business Card
Peter L. Vandrell CFB, CTB
48317 W 63rd Ave
Harlow Ridge, WA 99482
C +1 503.555.0147
O +1 808.555.0182
Peter@fieldlaneco.example
www.fieldlaneco.example

```html
<!DOCTYPE html>
<html lang="en">
<head>
<meta charset="utf-8">
<title>Corvane Sport – Business Card</title>
<link rel="stylesheet" href="https://fonts.googleapis.com/css2?family=Arimo:wght@400;700&family=Raleway:wght@200&display=swap">
<style>
  :root {
    --bg: #d6d6d3;
    --card-black: #0b0b0b;
    --drawing-tone: #1c1c1c;
    --orange: #f39a1e;
    --orange-deep: #e8890f;
    --ink: #111111;
    --white: #ffffff;
  }
  * { box-sizing: border-box; margin: 0; padding: 0; }
  html, body {
    width: 1200px; height: 1200px; overflow: hidden;
    background: var(--bg);
    font-family: "Arimo", Arial, sans-serif;
  }
  .card {
    position: absolute; left: 150px;
    width: 900px; height: 514px;
    overflow: hidden;
    box-shadow: 0 6px 18px rgba(0,0,0,.18);
  }
  .card--info { top: 56px; display: flex; }
  .card--brand { top: 630px; background: var(--card-black); }

  .plan-backdrop {
    position: absolute; inset: 0;
    background: radial-gradient(ellipse at 55% 45%, var(--drawing-tone) 0%, var(--card-black) 75%);
  }

  /* Company name (plain text, shared) */
  .company-name {
    display: inline-flex; align-items: center; gap: 14px;
    font-family: "Arimo", Arial, sans-serif; font-weight: 400;
    color: var(--orange); white-space: nowrap;
  }
  .company-name__dot {
    flex: none; border-radius: 50%; background: var(--orange);
  }

  /* Info side */
  .brand-strip {
    position: relative; width: 280px; height: 100%;
    background: var(--card-black);
  }
  .strip-name {
    position: absolute; left: 50%; top: 50%;
    transform: translate(-50%, -50%) rotate(-90deg);
    font-size: 36px;
  }
  .strip-name .company-name__dot { width: 22px; height: 22px; }

  .contact-panel {
    flex: 1; position: relative;
    background: linear-gradient(180deg, var(--orange) 0%, var(--orange-deep) 100%);
    padding: 34px 40px 0 48px;
  }
  .person-name {
    font-family: "Raleway", Arial, sans-serif;
    font-weight: 200; font-size: 72px; line-height: 1;
    color: var(--white); text-align: right;
    padding-right: 10px;
  }
  .person-title {
    font-weight: 700; font-size: 30px; color: var(--ink);
    margin: 6px 0 0 90px;
  }
  .contact-list { list-style: none; margin-top: 26px; }
  .contact-item {
    display: flex; align-items: flex-start; gap: 20px;
    font-size: 24px; line-height: 1.35; color: var(--ink);
    margin-bottom: 22px;
  }
  .contact-item svg { flex: none; width: 30px; height: 30px; margin-top: 2px; }

  /* Brand side */
  .card--brand .plan-backdrop { bottom: 114px; }
  .brand-center {
    position: absolute; left: 0; right: 0; top: 0; height: 400px;
    display: flex; flex-direction: column; align-items: center; justify-content: center;
    gap: 22px;
  }
  .brand-name { font-size: 64px; }
  .brand-name .company-name__dot { width: 30px; height: 30px; }
  .motto {
    font-size: 22px; color: var(--white);
  }
  .web-band {
    position: absolute; left: 0; right: 0; bottom: 0; height: 114px;
    background: linear-gradient(180deg, var(--orange) 0%, var(--orange-deep) 100%);
    display: flex; align-items: center; justify-content: center;
  }
  .web-address { font-size: 44px; color: var(--ink); }
</style>
</head>
<body>

<section class="card card--info">
  <div class="brand-strip">
    <div class="plan-backdrop" role="img" aria-label="Faint athletic facility site plan drawing behind the company name"></div>
    <div class="company-name strip-name"><span class="company-name__dot"></span>Corvane Sport</div>
  </div>
  <div class="contact-panel">
    <h1 class="person-name">Peter L.</h1>
    <p class="person-title">Vandrell CFB, CTB</p>
    <ul class="contact-list">
      <li class="contact-item">
        <svg viewBox="0 0 24 24" aria-hidden="true"><path d="M12 2a7 7 0 0 0-7 7c0 5 7 13 7 13s7-8 7-13a7 7 0 0 0-7-7zm0 9.5A2.5 2.5 0 1 1 12 6.5a2.5 2.5 0 0 1 0 5z" fill="none" stroke="#fff" stroke-width="1.6"/></svg>
        <span>48317 W 63rd Ave<br>Harlow Ridge, WA 99482</span>
      </li>
      <li class="contact-item">
        <svg viewBox="0 0 24 24" aria-hidden="true"><path d="M6.6 10.8a15 15 0 0 0 6.6 6.6l2.2-2.2a1 1 0 0 1 1-.25 11.4 11.4 0 0 0 3.6.57 1 1 0 0 1 1 1V20a1 1 0 0 1-1 1A17 17 0 0 1 3 4a1 1 0 0 1 1-1h3.5a1 1 0 0 1 1 1c0 1.25.2 2.45.57 3.6a1 1 0 0 1-.25 1z" fill="#fff"/></svg>
        <span>C +1 503.555.0147<br>O +1 808.555.0182</span>
      </li>
      <li class="contact-item">
        <svg viewBox="0 0 24 24" aria-hidden="true"><rect x="2" y="5" width="20" height="14" fill="#fff"/><path d="M2 5l10 8 10-8" fill="none" stroke="#e8890f" stroke-width="1.4"/></svg>
        <span>Peter@fieldlaneco.example</span>
      </li>
    </ul>
  </div>
</section>

<section class="card card--brand">
  <div class="plan-backdrop" role="img" aria-label="Faint athletic facility site plan drawing with running track outline"></div>
  <div class="brand-center">
    <div class="company-name brand-name"><span class="company-name__dot"></span>Corvane Sport</div>
    <p class="motto">True Owner Representation</p>
  </div>
  <div class="web-band">
    <p class="web-address">www.fieldlaneco.example</p>
  </div>
</section>

</body>
</html>
```